Brochure - Silver Harbor Circle

We need a brochure (tri-fold or bi-fold) for our network marketing company, Silver Harbor Circle. The brochure will be used for our Promoters (Distributors) to hand out to prospective customers and Promoters explaining our service as well as the income opportunity.

Industry/Entity Type

Club

```html
<!DOCTYPE html>
<html lang="en">
<head>
<meta charset="utf-8">
<title>Silver Harbor Circle – Tri-fold Brochure</title>
<link rel="stylesheet" href="https://fonts.googleapis.com/css2?family=Questrial&family=Oswald:wght@500;600&family=Raleway:wght@400;600;700;800&display=swap">
<style>
  :root{
    --blue:#1f95d8;
    --blue-dark:#1479b8;
    --green:#6cc436;
    --grey-text:#8a8f94;
    --dark:#3d4449;
    --panel-tint:#eef3f7;
    --paper:#ffffff;
    --stage:#e9eaeb;
    --photo-sky:#c9d6e2;
    --photo-house:#b8b2a8;
  }
  *{box-sizing:border-box;margin:0;padding:0}
  html,body{width:1200px;height:1200px;overflow:hidden}
  body{background:var(--stage);font-family:"Questrial",sans-serif;position:relative}
  .brochure{position:absolute;left:45px;top:150px;width:1110px;height:900px;display:flex;background:var(--paper);box-shadow:0 10px 30px rgba(0,0,0,.12)}
  .panel{position:relative;width:370px;height:900px;overflow:hidden}
  .panel + .panel{border-left:1px solid #e3e7ea}
  .decor{position:absolute;left:0;top:0;width:370px;height:900px}
  .bottom-rule{position:absolute;left:0;bottom:18px;width:100%;height:5px;background:var(--blue)}

  /* Panel 1 */
  .how-title{position:absolute;left:80px;top:340px;color:var(--blue);font-size:30px}
  .how-dot{position:absolute;left:38px;top:340px;width:32px;height:32px;border-radius:50%;background:var(--green)}
  .step{position:absolute;left:20px;width:340px;height:130px}
  .step-icon{position:absolute;left:0;top:22px;width:78px;height:78px;border-radius:50%;background:#fff;border:5px solid var(--blue);display:flex;align-items:center;justify-content:center}
  .step-pill{position:absolute;left:60px;top:0;width:280px;height:42px;border-radius:0 21px 21px 0;background:var(--blue);color:#fff;font-size:19px;line-height:42px;padding-left:36px}
  .step-text{position:absolute;left:98px;top:52px;width:225px;font-size:13.5px;line-height:1.3;color:var(--dark)}

  /* Panel 2 */
  .panel.services{background:var(--panel-tint)}
  .badge{position:absolute;left:130px;top:80px;width:110px;height:110px;border-radius:50%;background:var(--dark);border:6px solid #fff;box-shadow:0 0 0 4px var(--blue)}
  .tagline{position:absolute;left:0;width:100%;top:228px;text-align:center;color:var(--blue);font-size:30px}
  .services-head{position:absolute;left:0;width:100%;top:284px;text-align:center;color:var(--blue);font-size:26px}
  .services-head::before,.services-head::after{content:"";position:absolute;top:17px;width:95px;height:2px;background:var(--blue)}
  .services-head::before{left:30px}
  .services-head::after{right:30px}
  .service-list{position:absolute;left:22px;top:340px;width:330px;display:flex;flex-wrap:wrap;gap:6px 12px;align-content:flex-start;line-height:1.05;text-transform:uppercase}
  .svc{font-size:27px}
  .svc.bold{font-family:"Raleway",sans-serif;font-weight:800}
  .svc.cond{font-family:"Oswald",sans-serif;font-weight:600}
  .svc.thin{font-family:"Questrial",sans-serif}
  .svc.b{color:var(--blue)} .svc.g{color:var(--green)} .svc.k{color:var(--grey-text)}
  .svc.lower{text-transform:none}

  /* Panel 3 */
  .brand{position:absolute;right:26px;top:44px;text-align:right;color:var(--blue);font-family:"Raleway",sans-serif;font-weight:800;font-size:30px;line-height:1.05;letter-spacing:-.5px}
  .thumb{position:absolute;border-radius:50%;border:4px solid #fff;box-shadow:0 2px 6px rgba(0,0,0,.15)}
  .cover-copy{position:absolute;left:26px;top:700px;width:320px}
  .cover-lead{font-size:17px;line-height:1.35;color:var(--dark)}
  .cover-lead strong{font-family:"Raleway",sans-serif;font-weight:700;font-size:21px;color:var(--dark)}
  .cover-note{margin-top:16px;font-size:14px;line-height:1.35;color:var(--blue)}
</style>
</head>
<body>
<main class="brochure">

  <!-- Inside left: How it works -->
  <section class="panel how-it-works">
    <svg class="decor" viewBox="0 0 370 900" aria-hidden="true">
      <defs>
        <linearGradient id="houseA" x1="0" y1="0" x2="0" y2="1">
          <stop offset="0" stop-color="#c5d3e0"/><stop offset=".55" stop-color="#a8a49c"/><stop offset="1" stop-color="#8c7f70"/>
        </linearGradient>
      </defs>
      <polygon points="0,0 370,0 370,255 0,235" fill="url(#houseA)" role="img" aria-label="Photo of a two-storey suburban house at dusk"/>
      <polygon points="0,0 130,0 0,95" fill="var(--blue)"/>
      <polygon points="0,200 370,250 370,290 0,265" fill="var(--blue)"/>
      <polygon points="0,175 45,170 90,240 0,230" fill="var(--green)"/>
      <polygon points="300,245 370,255 370,270" fill="var(--green)"/>
    </svg>
    <span class="how-dot"></span>
    <h2 class="how-title">How it Works</h2>

    <div class="step" style="top:420px">
      <div class="step-pill">Describe Your Need</div>
      <div class="step-icon">
        <svg width="34" height="44" viewBox="0 0 34 44"><rect x="3" y="3" width="28" height="38" rx="14" fill="var(--blue)"/><line x1="17" y1="3" x2="17" y2="16" stroke="#fff" stroke-width="2"/></svg>
      </div>
      <p class="step-text">Choose your service category and tell us about your project with just a few mouse clicks.</p>
    </div>

    <div class="step" style="top:565px">
      <div class="step-pill">Name Your Price</div>
      <div class="step-icon">
        <svg width="44" height="40" viewBox="0 0 44 40"><path d="M4 4h28v20H14l-8 7v-7H4z" fill="var(--blue)"/><path d="M18 14h22v16h-4v6l-7-6H18z" fill="#7cc3ec"/><text x="11" y="20" font-size="13" fill="#fff" font-family="Questrial,sans-serif">$</text></svg>
      </div>
      <p class="step-text">We'll tell you the average price your neighbors have paid and you tell us what you want to pay.</p>
    </div>

    <div class="step" style="top:710px">
      <div class="step-pill">Get it Done!</div>
      <div class="step-icon">
        <svg width="40" height="40" viewBox="0 0 40 40"><path d="M6 21l9 9L34 9" fill="none" stroke="var(--blue)" stroke-width="6" stroke-linecap="round" stroke-linejoin="round"/></svg>
      </div>
      <p class="step-text">Within minutes, you'll receive acceptance of your project and price from one of SHC's network of service professionals in your area.</p>
    </div>
    <div class="bottom-rule"></div>
  </section>

  <!-- Inside middle: Services -->
  <section class="panel services">
    <svg class="decor" viewBox="0 0 370 900" aria-hidden="true">
      <g fill="#dfe8ef">
        <circle cx="60" cy="140" r="48"/><circle cx="300" cy="120" r="40"/><circle cx="90" cy="330" r="55"/>
        <circle cx="290" cy="430" r="60"/><circle cx="70" cy="560" r="50"/><circle cx="260" cy="650" r="45"/>
        <circle cx="120" cy="780" r="55"/><circle cx="310" cy="820" r="48"/>
      </g>
      <polygon points="0,0 60,0 0,120" fill="var(--blue)"/>
      <polygon points="0,120 60,0 100,0 0,175" fill="var(--blue)" opacity=".55"/>
      <polygon points="0,215 70,225 55,260 0,250" fill="var(--green)"/>
      <polygon points="310,0 370,0 370,40" fill="var(--green)"/>
    </svg>
    <div class="badge" aria-hidden="true"></div>
    <h2 class="tagline">The Best for Less</h2>
    <h3 class="services-head">Services</h3>
    <div class="service-list">
      <span class="svc cond g">Plastering</span>
      <span class="svc thin g lower">Past Control</span>
      <span class="svc bold b">Plumbing</span>
      <span class="svc thin k">Fencing</span>
      <span class="svc cond b">Chimney Sweep</span>
      <span class="svc bold g">Garage Doors</span>
      <span class="svc cond g">Deck &amp; Patios</span>
      <span class="svc bold b">Drywall</span>
      <span class="svc bold b">Siding</span>
      <span class="svc cond g">Roofing</span>
      <span class="svc bold b">Painting</span>
      <span class="svc thin k">Pool &amp; Hot Tub</span>
      <span class="svc cond g">Appliance Repair</span>
      <span class="svc cond b">Flooring</span>
      <span class="svc thin k">Yard Care</span>
      <span class="svc cond g">Heating &amp; Cooling</span>
      <span class="svc thin k">Carpet Cleaning</span>
      <span class="svc cond b">Windows &amp; Doors</span>
      <span class="svc cond g">Gutters</span>
      <span class="svc thin k">Countertops</span>
      <span class="svc cond b">Insulation</span>
    </div>
    <div class="bottom-rule"></div>
  </section>

  <!-- Cover panel -->
  <section class="panel cover">
    <svg class="decor" viewBox="0 0 370 900" aria-hidden="true">
      <defs>
        <linearGradient id="houseB" x1="0" y1="0" x2="0" y2="1">
          <stop offset="0" stop-color="#dfe5ea"/><stop offset=".5" stop-color="#c9c7c2"/><stop offset="1" stop-color="#b3b6b2"/>
        </linearGradient>
      </defs>
      <polygon points="0,150 370,150 370,560 0,560" fill="url(#houseB)" role="img" aria-label="Photo of a white stucco house with a stone chimney"/>
      <polygon points="0,0 370,0 370,230 230,330 0,150" fill="var(--paper)"/>
      <polygon points="0,120 240,265 230,330 0,175" fill="var(--green)"/>
      <polygon points="370,180 370,300 240,270" fill="var(--blue)"/>
      <polygon points="0,560 90,520 180,470 370,580 370,900 0,900" fill="#f2f6fa"/>
      <polygon points="150,470 370,590 370,650 150,505" fill="var(--blue)"/>
      <polygon points="40,540 150,470 150,505 60,555" fill="var(--green)"/>
      <polygon points="0,555 370,650 370,660 0,570" fill="var(--blue)" opacity=".25"/>
    </svg>
    <div class="brand">Silver Harbor<br>Circle</div>
    <div class="thumb" style="left:150px;top:520px;width:100px;height:100px;background:radial-gradient(circle,#c98d66,#7a4b33)" role="img" aria-label="Photo of a hand applying a caulking gun"></div>
    <div class="thumb" style="left:50px;top:590px;width:105px;height:105px;background:radial-gradient(circle,#d6d9dc,#8d8f90)" role="img" aria-label="Photo of a house wrapped in renovation scaffolding"></div>
    <div class="thumb" style="left:150px;top:620px;width:72px;height:72px;background:radial-gradient(circle,#b79a6b,#5b4630)" role="img" aria-label="Photo of plumbing pipes and fittings"></div>
    <div class="cover-copy">
      <p class="cover-lead"><strong>Don't worry</strong> be happy about what you pay for home projects! Our service lets you say what you pay!</p>
      <p class="cover-note">Home maintenance and repairs can be stressful. Who do I call? What will it cost? Will my price be fair?</p>
    </div>
    <div class="bottom-rule"></div>
  </section>

</main>
</body>
</html>
```